Bakery Business Cards

We are in need of business cards for our bakery business--something non-generic that reflects our business and will stand out. We are a wholesale bakery that primarily services in-store bakeries, casinos, schools, distributors, and fund-raising companies. The family business was founded in 1960. (www.marlowsovenworks.com)

```html
<!DOCTYPE html>
<html lang="en">
<head>
<meta charset="utf-8">
<title>Marlow's Ovenworks – Business Cards</title>
<link rel="stylesheet" href="https://fonts.googleapis.com/css2?family=Arimo:wght@400;700&display=swap">
<style>
  :root {
    --backdrop: #e8e8ea;
    --card: #2c2c2f;
    --card-pattern-a: #2a2a2d;
    --card-pattern-b: #323236;
    --brand-blue: #0b3fd8;
    --text-light: #f2f2f2;
    --rule: #bdbdc2;
  }
  * { box-sizing: border-box; margin: 0; padding: 0; }
  html, body { width: 1200px; height: 802px; overflow: hidden; }
  body {
    background: var(--backdrop);
    font-family: "Arimo", Arial, sans-serif;
    position: relative;
  }
  .card {
    position: absolute;
    top: 246px;
    width: 540px;
    height: 310px;
    background: var(--card);
    border-radius: 3px;
    overflow: hidden;
  }
  .card--front { left: 40px; }
  .card--back { left: 620px; }

  .front__brand {
    position: absolute;
    left: 0; top: 0;
    width: 250px; height: 310px;
    display: flex; align-items: center; justify-content: center;
    gap: 10px;
  }
  .brand-dot {
    width: 12px; height: 12px; border-radius: 50%;
    background: var(--brand-blue);
    flex: none;
  }
  .brand-name {
    color: var(--brand-blue);
    font-weight: 700;
    font-size: 27px;
    line-height: 1.1;
  }
  .front__divider {
    position: absolute;
    left: 262px; top: 66px;
    width: 1.5px; height: 178px;
    background: var(--rule);
  }
  .front__details {
    position: absolute;
    left: 290px; top: 66px;
    color: var(--text-light);
    font-size: 14px;
    line-height: 1.35;
  }
  .person-name {
    color: var(--brand-blue);
    font-size: 15px;
    letter-spacing: 0.5px;
    text-transform: uppercase;
  }
  .person-role { margin-bottom: 14px; }
  .address { margin-bottom: 14px; }
  .contact-list { list-style: none; }
  .contact-list li { display: flex; align-items: center; gap: 8px; }
  .contact-list svg { width: 12px; height: 12px; flex: none; }

  .back__pattern {
    position: absolute; inset: 0;
    background: linear-gradient(135deg, var(--card-pattern-a), var(--card-pattern-b) 50%, var(--card-pattern-a));
  }
  .back__brand {
    position: absolute; inset: 0;
    display: flex; align-items: center; justify-content: center;
    gap: 14px;
  }
  .back__brand .brand-dot { background: var(--text-light); width: 16px; height: 16px; }
  .back__brand .brand-name { color: var(--text-light); font-size: 38px; }
</style>
</head>
<body>
  <section class="card card--front" aria-label="Business card front">
    <div class="front__brand">
      <span class="brand-dot"></span>
      <span class="brand-name">Marlow's<br>Ovenworks</span>
    </div>
    <div class="front__divider"></div>
    <div class="front__details">
      <p class="person-name">Daniel Reyes</p>
      <p class="person-role">Manager</p>
      <p class="address">Your Address, City<br>State, Zip 0000</p>
      <ul class="contact-list">
        <li>
          <svg viewBox="0 0 12 12" aria-hidden="true"><path d="M2.5 1 L4.5 1 L5.2 3.5 L4 4.5 Q5 7 7.5 8 L8.5 6.8 L11 7.5 L11 9.5 Q10.5 11 9 11 Q1 10 1 2.5 Q1 1 2.5 1 Z" fill="#0b3fd8"/></svg>
          555-238-4417
        </li>
        <li>
          <svg viewBox="0 0 12 12" aria-hidden="true"><rect x="0.5" y="2" width="11" height="8" rx="1" fill="#0b3fd8"/><path d="M1 2.8 L6 6.5 L11 2.8" stroke="#2c2c2f" stroke-width="1" fill="none"/></svg>
          hello@marlowsovenworks.com
        </li>
        <li>
          <svg viewBox="0 0 12 12" aria-hidden="true"><circle cx="6" cy="6" r="5.5" fill="#0b3fd8"/><path d="M0.5 6 H11.5 M6 0.5 V11.5 M6 0.5 Q2.5 6 6 11.5 M6 0.5 Q9.5 6 6 11.5" stroke="#2c2c2f" stroke-width="0.8" fill="none"/></svg>
          www.marlowsovenworks.com
        </li>
      </ul>
    </div>
  </section>

  <section class="card card--back" aria-label="Business card back">
    <div class="back__pattern" role="img" aria-label="Embossed repeating pattern of chef hats"></div>
    <div class="back__brand">
      <span class="brand-dot"></span>
      <span class="brand-name">Marlow's<br>Ovenworks</span>
    </div>
  </section>
</body>
</html>
```